Modern Retail Coffee Label for established Roastery! 17 years!

We are looking for a Retail Coffee Bag Label... JUST THE LABEL TO GO ON AN EXISTING BAG. Our current label is provided and our Logo.. we have had the same Red Bags FOREVER so we are looking for a label to compliment that tradition and to be placed on the bags we have used for 17 years.

We have a retail line of bags with locally roasted coffee. Our business has been around 17years and is in need of a design upgrade! We have a red coffee bag and are looking for a sleek modern label. I will attach a file of our label right now so you can see what it looks like. We are just looking for a more modern version. a few inclusions:

Locally Roasted
100% Arabica Coffee
Heron Kin's Coffee
heronkincoffee.example
logo

The black label with the red and yellow color label is the old one... the new label should be the White background and black border one...

Target Market(s)

Retail Coffee Consumers

Font styles to use
Other font styles liked:
• use what you think. we are located in SW Wisconsin but ship coffee EVERYWHERE

Colors

Designer to choose only greyscale colors for use in the design.

Requirements
Must have
• Locally Roasted (Platteville,WI)
• 100% Arabica Coffee
• heronkincoffee.example
• logo
Nice to have
• Badgers
• "Since 2003"
Should not have
• Any lunabrew or big brand themes

```html
<!DOCTYPE html>
<html lang="en">
<head>
<meta charset="utf-8">
<title>Heron Kin Coffee – Arabica Label</title>
<link href="https://fonts.googleapis.com/css2?family=New+Rocker&family=Oswald:wght@500;600&display=swap" rel="stylesheet">
<style>
  :root {
    --page: #ecebe8;
    --label-dark: #383838;
    --label-white: #ffffff;
    --ink: #2b2b2b;
    --accent-grey: #a6a6a6;
    --bean-dark: #5a5a5a;
    --bean-light: #b8b8b8;
  }
  html, body {
    margin: 0;
    padding: 0;
    width: 1200px;
    height: 1200px;
    overflow: hidden;
    background: var(--page);
  }
  .label {
    position: relative;
    width: 1200px;
    height: 1200px;
  }
  .label-shape {
    position: absolute;
    inset: 0;
  }
  .label-content {
    position: absolute;
    inset: 0;
    display: flex;
    flex-direction: column;
    align-items: center;
    color: var(--label-white);
  }
  .tagline {
    margin: 232px 0 0;
    font-family: "Oswald", sans-serif;
    font-weight: 600;
    font-size: 22px;
    letter-spacing: 1px;
    text-transform: uppercase;
  }
  .brand-plate {
    margin-top: 24px;
    width: 300px;
    padding: 12px 0 10px;
    background: var(--label-white);
    border: 5px solid var(--ink);
    border-radius: 8px;
    box-shadow: 0 0 0 4px var(--label-white);
    color: var(--ink);
    font-family: "Oswald", sans-serif;
    font-weight: 500;
    text-align: center;
    text-transform: uppercase;
  }
  .brand-name {
    font-size: 42px;
    line-height: 1;
    letter-spacing: 1px;
  }
  .brand-divider {
    display: flex;
    align-items: center;
    justify-content: center;
    gap: 10px;
    margin: 8px 18px;
  }
  .brand-divider::before,
  .brand-divider::after {
    content: "";
    flex: 1;
    height: 3px;
    background: var(--accent-grey);
  }
  .brand-dot {
    width: 20px;
    height: 20px;
    border-radius: 50%;
    background: var(--accent-grey);
  }
  .brand-sub {
    font-size: 40px;
    line-height: 1;
    letter-spacing: 1px;
  }
  .percent {
    margin-top: 34px;
    display: flex;
    align-items: center;
    gap: 22px;
    font-family: "Oswald", sans-serif;
    font-weight: 500;
    font-size: 34px;
    line-height: 1.2;
  }
  .percent::before,
  .percent::after {
    content: "";
    width: 110px;
    height: 3px;
    background: var(--label-white);
  }
  .product-name {
    margin-top: 2px;
    font-family: "New Rocker", serif;
    font-size: 120px;
    line-height: 1;
    letter-spacing: 0;
    text-transform: uppercase;
  }
  .product-type {
    margin-top: 0;
    font-family: "New Rocker", serif;
    font-size: 128px;
    line-height: 1;
    letter-spacing: 2px;
  }
  .bean-art {
    margin-top: 18px;
    width: 240px;
    height: 86px;
    border-radius: 50% 50% 40% 40%;
    background: radial-gradient(ellipse at 50% 40%, var(--bean-light), var(--bean-dark));
  }
  .website {
    margin: 16px 0 0;
    font-family: "Oswald", sans-serif;
    font-weight: 500;
    font-size: 20px;
    letter-spacing: 1px;
  }
</style>
</head>
<body>
  <main class="label">
    <svg class="label-shape" viewBox="0 0 1200 1200" aria-hidden="true">
      <defs>
        <polygon id="shield" points="600,80 960,215 960,330 1005,420 1005,800 960,865 600,1120 240,865 195,800 195,420 240,330 240,215"/>
      </defs>
      <use href="#shield" fill="var(--label-dark)"/>
      <use href="#shield" fill="var(--label-white)" transform="translate(600 600) scale(0.975) translate(-600 -600)"/>
      <use href="#shield" fill="var(--label-dark)" transform="translate(600 600) scale(0.925) translate(-600 -600)"/>
      <use href="#shield" fill="none" stroke="var(--label-white)" stroke-width="5" transform="translate(600 600) scale(0.895) translate(-600 -600)"/>
    </svg>

    <div class="label-content">
      <p class="tagline">Locally Roasted</p>
      <div class="brand-plate">
        <div class="brand-name">Heron Kin</div>
        <div class="brand-divider"><span class="brand-dot"></span></div>
        <div class="brand-sub">Coffee</div>
      </div>
      <div class="percent">100%</div>
      <div class="product-name">Arabica</div>
      <div class="product-type">coffee</div>
      <div class="bean-art" role="img" aria-label="Illustration of two roasted coffee beans"></div>
      <p class="website">heronkincoffee.example</p>
    </div>
  </main>
</body>
</html>
```